Womens Personal Training studio needs new year flyers

I need a double sided A5 flyer to attract Women / Mothers to my fitness business, Radiant Core Studio, in the new year.

My business colour is teal, I am located in Oakvale QLD Aus

Exclusive studio training for women. At Radiant Core Studio we don't make New years resolutions, we Empower you to make the changes for life!

examples of pain Q's: Do you feel guilty about wanting to do something for yourself? Do you worry about what exercises are safe post baby? Are you struggling to regain control of your body and your life?

Would you like to love yourself and your body as much as you lvoe your baby?

I work with women to apporpriately and progressivley rebuild their bodies post preganany. As the Leading specialist in Pre and Post Natal Rehabilitation and Fitness in Durnford, Marnie knows what it takes to find the right balance. With a vision of Empowering this generation to inspire the next, Marnie teaches skills for LIFE so you can lead your family to a Healthier, Fitter and Stronger future! Using a fusion of Pilates, Strength Conditioning and Cardio Marnie customises a plan for each individual. Your free consultation is waiting call now and learn the first steps to making the change Valued at $147 Don’t Miss out!! Marnie 0438 270 614

Quote to go with image "Marnie doesn't just help you achieve your weight loss goals she works with you to make sure you are 'Radiant Core Studio'." Tessa Brook July 2013

Target Market(s)

Women / Mothers

Industry/Entity Type

Training

Requirements
Must have
• call to action
contact details
Marnie Clarke
0438 270 614
marnie@radiantcorestudio.net.au
www.radiantcorestudio.net.au

```html
<!DOCTYPE html>
<html lang="en">
<head>
<meta charset="UTF-8">
<title>Radiant Core Studio – Flyer</title>
<link href="https://fonts.googleapis.com/css2?family=Alegreya:wght@400;500&display=swap" rel="stylesheet">
<style>
  :root {
    --teal: #0e8a8a;
    --teal-deep: #138787;
    --pink: #f07fb4;
    --ink: #000000;
    --paper: #ffffff;
    --frame: #555555;
    --photo-light: #f6f1f3;
    --photo-mid: #e2d8de;
  }
  * { margin: 0; padding: 0; box-sizing: border-box; }
  html, body {
    width: 1200px; height: 1000px; overflow: hidden;
    background: var(--paper);
    font-family: "Alegreya", Georgia, serif;
  }
  .canvas { position: relative; width: 1200px; height: 1000px; }
  .flyer {
    position: absolute; left: 245px; top: 0;
    width: 709px; height: 1000px;
    border: 1px solid var(--frame);
    background: var(--paper);
    overflow: hidden;
  }
  .flyer__decor { position: absolute; inset: 0; }
  .brand {
    position: absolute; left: 163px; top: 62px;
    display: flex; align-items: center; gap: 14px;
    color: var(--teal);
    font-size: 44px; font-weight: 500; letter-spacing: 0.5px;
  }
  .brand__dot {
    width: 34px; height: 34px; border-radius: 50%;
    background: var(--teal);
  }
  .photo {
    position: absolute; left: 55px; top: 185px;
    width: 260px; height: 560px;
    border-radius: 24px;
    background: radial-gradient(ellipse at 50% 45%, var(--photo-mid), var(--photo-light) 70%, var(--paper));
  }
  .about {
    position: absolute; left: 352px; top: 201px;
    width: 349px; height: 492px;
    background: var(--teal);
    border-radius: 22px;
    padding: 52px 16px 0 23px;
    color: var(--paper);
    font-size: 17.5px; line-height: 33px;
    text-align: justify; letter-spacing: 0.3px;
  }
  .cta {
    position: absolute; left: 0; top: 757px;
    width: 100%; height: 220px;
    background: var(--ink);
    padding: 21px 29px 0 37px;
    color: var(--teal-deep);
    font-size: 23.5px; line-height: 33px;
    text-align: justify; letter-spacing: 0.2px;
  }
  .cta__contact {
    margin-top: 6px;
    font-size: 16px; line-height: 22px;
    text-align: left; letter-spacing: 0.3px;
  }
</style>
</head>
<body>
<div class="canvas">
  <div class="flyer">
    <svg class="flyer__decor" width="709" height="1000" viewBox="0 0 709 1000" aria-hidden="true">
      <path d="M0 0 H720 C 330 20 60 90 0 385 Z" fill="var(--pink)"/>
    </svg>

    <div class="brand"><span>Radiant Core Studio</span><span class="brand__dot"></span></div>

    <div class="photo" role="img" aria-label="Photo of two women standing back to back in workout clothes, one pregnant and one after recovery"></div>

    <svg class="flyer__decor" width="709" height="1000" viewBox="0 0 709 1000" aria-hidden="true">
      <ellipse cx="175" cy="390" rx="172" ry="72" transform="rotate(-18 175 390)" fill="none" stroke="var(--teal)" stroke-width="4"/>
    </svg>

    <div class="about">
      As the Leading specialist in Pre and Post Natal Rehabilitation and Fitness in Durnford, Marnie knows what it takes to find the right balance&nbsp; With a vision of Empowering this generation to inspire the next, Marnie teaches&nbsp; skills for LIFE so you can lead your family to a Healthier, Fitter and Stronger&nbsp; future! Using a fusion of Pilates, Strength Conditioning and Cardio Marnie customises a plan for each individual
    </div>

    <div class="cta">
      <p class="cta__text">Your free consultation is waiting call now and learn the first steps to making the change Valued at $147 Don't Miss out!! Marnie 0438 270 614 "Marnie doesn't just help you achieve your weight loss goals she works&nbsp; with you to make sure you are 'Radiant Core Studio'."</p>
      <p class="cta__contact">Marnie Clarke &nbsp;·&nbsp; marnie@radiantcorestudio.net.au &nbsp;·&nbsp; www.radiantcorestudio.net.au</p>
    </div>
  </div>
</div>
</body>
</html>
```